Business Card for a Wedding Films Business

We require a business card design for our business 'Lewis Marrow Wedding Films'. The logo needs to look classy and high end.

Target Market(s)

Wedding Couples

Contact Information for Business Card

Lewis Marrow Wedding Films
07312 605 227
films@lewismarrowreels.com
www.lewismarrowreels.com

Facebook: @lewismarrowweddingfilms
Instagram: @lewismarrowfilms

Font styles to use
Sans Serif

Requirements
Must have
• Social media icons - Facebook and Instagram

```html
<!DOCTYPE html>
<html lang="en">
<head>
<meta charset="utf-8">
<title>Lewis Marrow Wedding Films – Business Card</title>
<link rel="stylesheet" href="https://fonts.googleapis.com/css2?family=Jost:wght@500&family=Source+Sans+3:wght@400&display=swap">
<style>
  :root {
    --backdrop: #e4e4e4;
    --card-dark: #1f1f1f;
    --card-light: #f4f4f4;
    --ink: #1a1a1a;
    --emboss: #3a3a3a;
  }
  * { margin: 0; padding: 0; box-sizing: border-box; }
  html, body {
    width: 1200px;
    height: 960px;
    overflow: hidden;
    background: var(--backdrop);
  }
  .canvas { position: relative; width: 1200px; height: 960px; }

  .card {
    position: absolute;
    left: 322px;
    width: 556px;
    height: 360px;
  }
  .card--front { top: 104px; background: var(--card-dark); }
  .card--back  { top: 495px; background: var(--card-light); color: var(--ink); }

  .front-name {
    position: absolute;
    left: 0; right: 0; top: 160px;
    text-align: center;
    font-family: "Jost", sans-serif;
    font-weight: 500;
    font-size: 26px;
    letter-spacing: 6px;
    color: var(--emboss);
  }

  .brand {
    position: absolute;
    left: 0; right: 0; top: 68px;
    text-align: center;
    font-family: "Jost", sans-serif;
    font-weight: 500;
    color: var(--ink);
  }
  .brand__mark {
    display: block;
    width: 40px; height: 40px;
    margin: 0 auto 34px;
    border: 3px solid var(--ink);
  }
  .brand__name {
    display: block;
    font-size: 28px;
    letter-spacing: 4.5px;
    line-height: 30px;
  }
  .brand__tagline {
    display: block;
    font-size: 14px;
    letter-spacing: 4.2px;
    line-height: 18px;
    margin-top: 4px;
  }

  .contacts {
    position: absolute;
    top: 246px;
    left: 0; right: 0;
    font-family: "Source Sans 3", sans-serif;
    font-size: 15px;
    line-height: 20px;
  }
  .contacts__direct {
    position: absolute;
    right: 291px;
    text-align: right;
  }
  .contacts__divider {
    position: absolute;
    left: 277px; top: 0;
    width: 1.5px; height: 42px;
    background: var(--ink);
  }
  .contacts__social {
    position: absolute;
    left: 289px;
  }
  .contact-line { display: flex; align-items: center; gap: 5px; white-space: nowrap; }
  .contacts__direct .contact-line { justify-content: flex-end; }
  .contact-line svg { width: 14px; height: 14px; flex: none; }
  .social-badge {
    width: 13px; height: 13px;
    background: var(--ink);
    border-radius: 2px;
    flex: none;
  }

  .website {
    position: absolute;
    left: 0; right: 0; top: 306px;
    text-align: center;
    font-family: "Source Sans 3", sans-serif;
    font-size: 15px;
    letter-spacing: 1.2px;
  }
</style>
</head>
<body>
<div class="canvas">

  <section class="card card--front">
    <p class="front-name">LEWIS MARROW</p>
  </section>

  <section class="card card--back">
    <div class="brand">
      <span class="brand__mark"></span>
      <span class="brand__name">LEWIS MARROW</span>
      <span class="brand__tagline">WEDDING FILMS</span>
    </div>

    <div class="contacts">
      <div class="contacts__direct">
        <p class="contact-line">07312 605 227
          <svg viewBox="0 0 24 24" aria-hidden="true"><path fill="#1a1a1a" d="M6.6 10.8a15.1 15.1 0 0 0 6.6 6.6l2.2-2.2a1 1 0 0 1 1-.25 11.4 11.4 0 0 0 3.6.57 1 1 0 0 1 1 1V20a1 1 0 0 1-1 1A17 17 0 0 1 3 4a1 1 0 0 1 1-1h3.5a1 1 0 0 1 1 1c0 1.25.2 2.45.57 3.57a1 1 0 0 1-.25 1z"/></svg>
        </p>
        <p class="contact-line">films@lewismarrowreels.com
          <svg viewBox="0 0 24 24" aria-hidden="true"><rect x="2.5" y="5" width="19" height="14" fill="none" stroke="#1a1a1a" stroke-width="2"/><path d="M3 6l9 7 9-7" fill="none" stroke="#1a1a1a" stroke-width="2"/></svg>
        </p>
      </div>
      <span class="contacts__divider"></span>
      <div class="contacts__social">
        <p class="contact-line"><span class="social-badge"></span>@lewismarrowweddingfilms</p>
        <p class="contact-line"><span class="social-badge"></span>@lewismarrowfilms</p>
      </div>
    </div>

    <p class="website">www.lewismarrowreels.com</p>
  </section>

</div>
</body>
</html>
```